Pellham Ridge deaerator 25 Year

Reason: need individual names on business cards. Also need higher resolution.

Industry/Entity Type

Business

Contact Information for Business Card

See sample business card

```html
<!DOCTYPE html>
<html lang="en">
<head>
<meta charset="utf-8">
<title>Pellham Ridge deaerator – Business Card</title>
<link rel="stylesheet" href="https://fonts.googleapis.com/css2?family=Oswald:wght@300;400;500;600&family=Open+Sans:wght@400;600&display=swap">
<style>
  :root {
    --page: #e9e7e3;
    --grey-dark: #5e5e5e;
    --grey-mid: #7a7a7a;
    --grey-light: #8c8c8c;
    --paper: #f7f7f7;
    --paper-shade: #dedede;
    --ink: #3a3a3a;
    --on-grey: #ffffff;
    --on-grey-soft: #e4e4e4;
  }
  * { box-sizing: border-box; margin: 0; padding: 0; }
  html, body { width: 1200px; height: 970px; overflow: hidden; }
  body {
    background: var(--page);
    font-family: "Open Sans", Arial, sans-serif;
    display: flex;
    flex-direction: column;
    align-items: center;
    justify-content: center;
    gap: 40px;
  }
  .card {
    position: relative;
    width: 760px;
    height: 434px;
    overflow: hidden;
    box-shadow: 0 10px 28px rgba(0,0,0,.22);
  }

  /* Back of the card */
  .card-back { background: linear-gradient(90deg, var(--paper-shade), var(--paper) 55%, #ececec); }
  .card-back .band {
    position: absolute; left: 0; right: 0; height: 92px;
    background: linear-gradient(90deg, var(--grey-dark), var(--grey-light));
  }
  .card-back .band-top { top: 0; }
  .card-back .band-bottom { bottom: 0; }
  .card-back .brand { position: absolute; left: 0; right: 0; top: 92px; bottom: 92px; justify-content: center; }

  /* Brand lock-up */
  .brand { display: flex; align-items: center; gap: 18px; }
  .brand-dot {
    width: 58px; height: 58px; border-radius: 50%;
    background: var(--grey-mid);
    flex: none;
  }
  .brand-name {
    font-family: "Oswald", Arial, sans-serif;
    font-weight: 500;
    font-size: 40px;
    color: var(--ink);
    line-height: 1;
  }

  /* Front of the card */
  .card-front { background: linear-gradient(135deg, var(--grey-dark), var(--grey-light)); }
  .front-panel {
    position: absolute; left: 0; bottom: 0;
    width: 350px; height: 300px;
    background: linear-gradient(180deg, #ffffff, #ececec);
  }
  .front-panel::after {
    content: ""; position: absolute; right: -22px; top: 34px;
    border-top: 16px solid transparent;
    border-bottom: 16px solid transparent;
    border-left: 22px solid #fdfdfd;
  }
  .front-panel .brand {
    position: absolute; inset: 0; flex-direction: column; justify-content: center; gap: 14px;
  }
  .front-panel .brand-name { font-size: 30px; text-align: center; }

  .identity {
    position: absolute; left: 390px; top: 138px; right: 20px;
    display: flex; align-items: baseline; gap: 12px;
    white-space: nowrap;
  }
  .person-name {
    font-family: "Oswald", Arial, sans-serif;
    font-weight: 600; font-size: 28px; letter-spacing: .5px; line-height: 1.2;
    color: var(--on-grey); text-transform: uppercase;
  }
  .person-role {
    font-family: "Oswald", Arial, sans-serif;
    font-weight: 300; font-size: 16px; letter-spacing: 1.5px; line-height: 1.2;
    color: var(--on-grey-soft); text-transform: uppercase;
  }
  .contacts {
    position: absolute; left: 390px; top: 200px;
    list-style: none;
    display: grid; grid-template-columns: 170px 1fr; row-gap: 18px; column-gap: 10px;
  }
  .contacts li { display: flex; align-items: center; gap: 9px; font-size: 13px; color: var(--on-grey); white-space: nowrap; }
  .contacts li.wide { grid-column: 1 / 3; }
  .icon {
    width: 22px; height: 22px; border-radius: 50%;
    border: 1.5px solid var(--on-grey); flex: none;
    display: flex; align-items: center; justify-content: center;
  }
  .icon svg { width: 12px; height: 12px; fill: none; stroke: var(--on-grey); stroke-width: 1.8; stroke-linecap: round; stroke-linejoin: round; }
</style>
</head>
<body>

  <section class="card card-back" aria-label="Card back">
    <div class="band band-top"></div>
    <div class="brand">
      <span class="brand-dot"></span>
      <span class="brand-name">Pellham Ridge deaerator</span>
    </div>
    <div class="band band-bottom"></div>
  </section>

  <section class="card card-front" aria-label="Card front">
    <div class="front-panel">
      <div class="brand">
        <span class="brand-dot"></span>
        <span class="brand-name">Pellham Ridge<br>deaerator</span>
      </div>
    </div>

    <div class="identity">
      <span class="person-name">Alden Marsh</span>
      <span class="person-role">General Manager</span>
    </div>

    <ul class="contacts">
      <li>
        <span class="icon"><svg viewBox="0 0 12 12"><path d="M3 1.5 L4.8 3.6 L3.8 4.8 Q5 7 7.2 8.2 L8.4 7.2 L10.5 9 L9.2 10.5 Q4.5 10 1.5 2.8 Z"/></svg></span>
        014 552 3190
      </li>
      <li>
        <span class="icon"><svg viewBox="0 0 12 12"><rect x="1.5" y="3" width="9" height="6.5"/><path d="M1.5 3 L6 6.8 L10.5 3"/></svg></span>
        hello@ridgemail.net
      </li>
      <li>
        <span class="icon"><svg viewBox="0 0 12 12"><path d="M3 1.5 L4.8 3.6 L3.8 4.8 Q5 7 7.2 8.2 L8.4 7.2 L10.5 9 L9.2 10.5 Q4.5 10 1.5 2.8 Z"/></svg></span>
        014 552 3191
      </li>
      <li>
        <span class="icon"><svg viewBox="0 0 12 12"><circle cx="6" cy="6" r="4.5"/><path d="M1.5 6 H10.5 M6 1.5 Q3.5 6 6 10.5 M6 1.5 Q8.5 6 6 10.5"/></svg></span>
        www.pellhamridge.net
      </li>
      <li class="wide">
        <span class="icon"><svg viewBox="0 0 12 12"><path d="M6 11 Q2 6.5 2 4.5 A4 4 0 0 1 10 4.5 Q10 6.5 6 11 Z"/><circle cx="6" cy="4.5" r="1.3"/></svg></span>
        214 Oak Lane Road, 2nd building Street w.
      </li>
    </ul>
  </section>

</body>
</html>
```